Velvet Loom (E-commerce) Website for Embroidery shop

Briefing:

Velvet Loom is an online personalized embroidery shop targeting mainly three customer segments:
1) lovers and marring couples
2) close friends wishing to give unique gifts
3) moms with new born baby personalized gifts

These customers are being served through our three major business lines:
1) Bathrobes and towels with personalized embroidery
2) Embroidered pillows and cushions
3) baby gifts with costumed baby sets stitched

Requirements:

The business has been recently established with moderate variety of products introduced so far. The website must consists of four major pages; a home page and three pages for every single business line. All images necessary for the web design are shareable upon request for copyright reasons if necessary. Please post a few products in each page to make it easy for the employee to use as benchmarks to upload other products.

The website also should contain all items and buttons exist in any e-commerce website such as:

1- social links:
a. (Major) Instagram: https://www.instagram.com/velvet.loom.atelier/
b. Twitter: https://twitter.com/Velvet_Loom_
c. Facebook: https://www.facebook.com/Velvet.loom.atelier/
d. Snapchat: coming soon

2- Help:
a. Delivery & Returns (inside KSA)
I. Delivery:
- Rush: within 3 business days (SAR 90)
- Express: within 5 business days (SAR 65)
- Standard: 7-10 business days ( SAR 35)
II. Returns: We guarantee you will love our product. But if you don't like it, send it back to us within two days from delivery and we will donate it to a charity and return your money subject to our terms and conditions.

b. Contact:
- Email: Velvet.loom.atelier@stitchmail.example
- (Mobile) Whats-app: +966 55 321 9076 (for quick response)

d. Warranty:
for only SAR 20 per product, we will give you a lifetime warranty over our German stitches

3- Payment options:
bank transfer, visa, MasterCard and PayPal

Remarks:

- This website is mainly aimed at customers in Saudi Arabia where some contents may not appeal to people from such country and results in your participation being excluded from the contest.

- You are the expert and if I am a webdesigner, I would have not posted this contest, so please use your our own judgment and creativity to come up with the best experience possible.

- Use our Instagram account as your first reference to understand our business as it is our major channel that has been used to reach our customers. Please don't use the pictures with poor quality as we will be replacing them with other images with better quality.

- We intend to have this website bilingual (i.e English and Arabic), so if you can translate it into Arabic, then we will pay you an extra $100 in addition to the contest price.

- If in doubt, please feel free to ask any question and suggestions are always encouraged and warm welcomed.

- If you succeed in this contest, you will be chosen as our ultimate Web designer. That means you will have a long relationship providing services to our customers under one of our businesses that aims at preparing start-up companies establishing their business.

Target Market(s)

1) lovers and marrying couples

Industry/Entity Type

Embroidery

Number of Pages Required

4 page

Font styles to use
Serif
Script

Colors

Designer to choose colors to be used in the design.

Requirements
Must have
• Requirements:
• The business has been recently established with moderate variety of products introduced so far. The website must consists of four major pages; a home page and three pages for every single business line. All images necessary for the web design are shareable upon request for copyright reasons if necessary. Please post a few products in each page to make it easy for the employee to use as benchmarks to upload other products.
• The Website must be also mobile use friendly!!!
• The website also should contain all items and buttons exist in any e-commerce website such as:
• 1- social links:
• a. (Major) Instagram: https://www.instagram.com/velvet.loom.atelier/
• b. Twitter: https://twitter.com/Velvet_Loom_
• c. Facebook: https://www.facebook.com/Velvet.loom.atelier/
• d. Snapchat: coming soon
• 2- Help:
• a. Delivery & Returns (inside KSA)
• I. Delivery:
• - Rush: within 3 business days (SAR 90)
• - Express: within 5 business days (SAR 65)
• - Standard: 7-10 business days ( SAR 35)
• II. Returns: We guarantee you will love our product. But if you don't like it, send it back to us within two days from delivery and we will donate it to a charity and return your money subject to our terms and conditions.
• b. Contact:
• - Email: Velvet.loom.atelier@stitchmail.example
• - (Mobile) Whats-app: +966 55 321 9076 (for quick response)
• d. Warranty:
• for only SAR 20 per product, we will give you a lifetime warranty over our German stitches
• 3- Payment options:
• bank transfer, visa, MasterCard and PayPal
• Note: You will be responsible to upload the design to the website fully and ensure its integration and functionality.

```html
<!DOCTYPE html>
<html lang="en">
<head>
<meta charset="utf-8">
<title>Velvet Loom – Personalized Embroidery</title>
<link rel="stylesheet" href="https://fonts.googleapis.com/css2?family=Comfortaa:wght@300;400&family=Lato:wght@400;700;900&family=Roboto:wght@400;500&display=swap">
<style>
:root{
  --gold:#b38b45;
  --gold-dark:#9c7535;
  --ink:#333333;
  --muted:#7a7a7a;
  --light:#f1f1f1;
  --dark:#343434;
  --darker:#2b2b2b;
  --white:#ffffff;
  --btn-gray:#6f6f6f;
}
*{box-sizing:border-box;margin:0;padding:0}
html,body{width:1200px;height:3175px;overflow:hidden}
body{position:relative;font-family:'Lato',Arial,sans-serif;color:var(--ink);background:var(--white)}
.abs{position:absolute}
a{color:inherit;text-decoration:none}

/* header */
.site-header{position:absolute;left:0;top:0;width:1200px;height:152px;background:var(--white);z-index:3;box-shadow:0 2px 6px rgba(0,0,0,.08)}
.brand-panel{position:absolute;left:0;top:0}
.brand-name{position:absolute;left:82px;top:50px;font-family:'Lato',sans-serif;font-weight:700;font-size:34px;color:var(--white);letter-spacing:.5px}
.top-contact{position:absolute;top:26px;display:flex;align-items:center;gap:12px;font-family:'Roboto',sans-serif;font-size:16px;color:var(--ink)}
.icon-dot{width:34px;height:34px;border-radius:50%;display:flex;align-items:center;justify-content:center}
.icon-dot.gold{background:var(--gold)}
.icon-dot.gray{background:#777}
.lang{position:absolute;left:1020px;top:26px;width:82px;height:30px;border:1px solid #ccc;display:flex;align-items:center;gap:6px;padding-left:6px;font-size:14px;font-family:'Roboto',sans-serif}
.flag{width:28px;height:18px;background:linear-gradient(135deg,#2a4a9a 0 40%,#fff 40% 48%,#c8263a 48% 56%,#fff 56% 64%,#2a4a9a 64%)}
.main-nav{position:absolute;top:96px;left:0;width:1200px;height:30px}
.main-nav a{position:absolute;font-family:'Roboto',sans-serif;font-size:17px;font-weight:500;color:#222}
.main-nav a.active{color:var(--gold)}

/* hero */
.hero{position:absolute;left:0;top:152px;width:1200px;height:525px;overflow:hidden}
.hero-photo{position:absolute;inset:0;background:
  radial-gradient(ellipse 380px 260px at 780px 230px,#e9e6ec 0%,rgba(233,230,236,0) 70%),
  radial-gradient(ellipse 260px 120px at 820px 120px,#8b7a9c 0%,rgba(139,122,156,0) 75%),
  linear-gradient(90deg,#6d6d6d 0%,#8d8d8d 45%,#a9a5ac 70%,#7c7c7c 100%)}
.hero-title{position:absolute;left:98px;top:118px;font-family:'Comfortaa',sans-serif;font-weight:300;font-size:62px;color:var(--white);letter-spacing:-1px}
.hero-copy{position:absolute;left:100px;top:225px;font-size:19px;line-height:33px;color:var(--white)}
.btn-outline{position:absolute;left:100px;top:324px;width:129px;height:46px;border:2px solid #e6d2ad;background:var(--gold);color:var(--white);font-size:17px;display:flex;align-items:center;justify-content:center}
.slider-arrow{position:absolute}
.hero-wave{position:absolute;left:0;top:430px}

/* section headings */
.sec-title{position:absolute;left:0;width:1200px;text-align:center;font-weight:700;font-size:26px;color:var(--gold);letter-spacing:.3px}
.sec-rule{position:absolute;left:537px;width:127px;height:2px;background:var(--gold)}

/* segments */
.segment{position:absolute;top:880px;width:323px;height:220px;border:3px solid #e2e2e2;border-radius:6px;overflow:hidden}
.segment .fill{position:absolute;inset:0}
.segment-caption{position:absolute;top:1124px;width:323px;text-align:center;font-size:19px;line-height:29px;color:#333}
.shop-now{position:absolute;left:82px;top:85px;width:155px;height:44px;background:#3b2c1a;border:2px solid #e7dccb;color:var(--white);font-family:'Roboto',sans-serif;font-weight:500;font-size:19px;display:flex;align-items:center;justify-content:center;z-index:2}

/* products */
.products-band{position:absolute;left:0;top:1248px;width:1200px;height:625px;background:radial-gradient(ellipse 700px 320px at 600px 310px,#ffffff 0%,#f3f3f3 70%,#e9e9e9 100%)}
.product-card{position:absolute;top:1422px;width:230px;height:362px;background:var(--white);border:1px solid #dddddd}
.product-card .thumb{height:193px}
.product-name{margin-top:22px;text-align:center;font-size:17px;color:var(--gold)}
.product-desc{margin:10px auto 0;width:190px;text-align:center;font-size:11px;line-height:14px;color:var(--muted)}
.product-foot{position:absolute;left:20px;right:20px;top:306px;display:flex;justify-content:space-between;align-items:center}
.price{font-size:20px;color:var(--muted)}
.price.gold{color:var(--gold)}
.btn-cart{width:112px;height:36px;background:var(--btn-gray);color:var(--white);font-size:13px;display:flex;align-items:center;justify-content:center;border-radius:2px}
.btn-cart.gold{background:var(--gold)}

/* gallery */
.gallery-band{position:absolute;left:0;top:1873px;width:1200px;height:571px;background:linear-gradient(180deg,#3a3a3a,#2f2f2f 60%,#3b3b3b)}
.gallery-title{position:absolute;left:0;top:62px;width:1200px;text-align:center;color:var(--white);font-weight:700;font-size:26px}
.gallery-rule{position:absolute;left:560px;top:110px;width:80px;height:3px;background:var(--white)}
.gallery-item{position:absolute;border:2px solid #e8e8e8}

/* features */
.feature{position:absolute;top:2518px;display:flex;gap:18px}
.feature-badge{width:94px;height:94px;border-radius:50%;background:var(--gold);border:4px solid #e9dcc3;box-shadow:0 0 0 2px var(--gold);display:flex;align-items:center;justify-content:center;flex-shrink:0}
.feature h3{font-size:20px;font-weight:700;color:#333;margin-top:10px;letter-spacing:.3px}
.feature p{font-size:12px;line-height:19px;color:#666;margin-top:6px;width:220px}

/* footer */
.footer-wave{position:absolute;left:0;top:2640px}
.site-footer{position:absolute;left:0;top:2760px;width:1200px;height:415px;background:var(--dark)}
.footer-brand{position:absolute;left:100px;top:150px;display:flex;align-items:center;gap:12px;font-weight:700;font-size:34px;color:var(--white)}
.footer-brand .dot{width:18px;height:18px;border-radius:50%;background:var(--white)}
.footer-head{position:absolute;top:72px;font-weight:700;font-size:17px;color:var(--white);letter-spacing:.3px}
.footer-head::after{content:"";position:absolute;left:0;top:30px;width:110px;height:1px;background:#777}
.link-list{position:absolute;left:372px;top:128px;list-style:none}
.link-list li{font-size:15px;color:var(--white);height:31px}
.contact-row{position:absolute;left:548px;display:flex;gap:18px}
.ring{width:34px;height:34px;border:2px solid var(--white);border-radius:50%;display:flex;align-items:center;justify-content:center;flex-shrink:0}
.contact-row strong{display:block;font-size:15px;color:var(--white)}
.contact-row span{display:block;font-size:13px;line-height:19px;color:#ddd}
.pay-box{position:absolute;left:836px;top:130px;width:260px;height:115px;background:var(--white);display:flex;align-items:center;justify-content:center;gap:10px;padding:10px}
.pay-chip{width:72px;height:48px;border-radius:4px}
.footer-bar{position:absolute;left:0;top:340px;width:1200px;height:1px;border-top:1px dashed #777}
.copyright{position:absolute;left:100px;top:366px;font-size:15px;color:var(--white)}
.social{position:absolute;left:925px;top:360px;display:flex;gap:8px}
.social span{width:34px;height:34px;border:2px solid var(--white);border-radius:50%}
</style>
</head>
<body>

<header class="site-header">
  <svg class="brand-panel" width="420" height="152" viewBox="0 0 420 152" aria-hidden="true">
    <polygon points="0,0 412,0 352,152 0,152" fill="#b38b45"/>
  </svg>
  <div class="brand-name">Velvet Loom</div>

  <div class="top-contact" style="left:498px">
    <span class="icon-dot gold"><svg width="16" height="12" viewBox="0 0 16 12"><rect x="1" y="1" width="14" height="10" fill="none" stroke="#fff" stroke-width="1.6"/><path d="M1 1 L8 7 L15 1" fill="none" stroke="#fff" stroke-width="1.6"/></svg></span>
    <a href="mailto:Velvet.loom.atelier@stitchmail.example">Velvet.loom.atelier@stitchmail.example</a>
  </div>
  <div class="top-contact" style="left:822px">
    <span class="icon-dot gray"><svg width="16" height="16" viewBox="0 0 16 16"><path d="M3 1 L6 1 L7 5 L5 6.5 C6 9 7 10 9.5 11 L11 9 L15 10 L15 13 C15 14 14 15 13 15 C6 15 1 10 1 3 C1 2 2 1 3 1Z" fill="#fff"/></svg></span>
    <span>+966 55 321 9076</span>
  </div>
  <div class="lang"><span class="flag" role="img" aria-label="English flag"></span>Eng ▾</div>

  <nav class="main-nav">
    <a class="active" href="#" style="left:448px">Home</a>
    <a href="#" style="left:554px">Embroidery</a>
    <a href="#" style="left:693px">Products</a>
    <a href="#" style="left:817px">Gallery</a>
    <a href="#" style="left:924px">Shop</a>
    <a href="#" style="left:1016px">Contact Us</a>
  </nav>
</header>

<section class="hero">
  <div class="hero-photo" role="img" aria-label="Folded white and lilac bathrobes with purple name embroidery and satin ribbons"></div>
  <h1 class="hero-title">Velvet Loom</h1>
  <p class="hero-copy">We are an embroidery shop in Saudi Arabia.<br>We focus on customer segments.</p>
  <a class="btn-outline" href="#">Read More</a>
  <svg class="slider-arrow" style="left:28px;top:246px" width="20" height="36" viewBox="0 0 20 36"><path d="M17 2 L3 18 L17 34" fill="none" stroke="#fff" stroke-width="3"/></svg>
  <svg class="slider-arrow" style="left:1152px;top:246px" width="20" height="36" viewBox="0 0 20 36"><path d="M3 2 L17 18 L3 34" fill="none" stroke="#fff" stroke-width="3"/></svg>
  <svg class="hero-wave" width="1200" height="95" viewBox="0 0 1200 95" aria-hidden="true">
    <path d="M0 40 C250 70 520 92 760 82 C950 74 1100 40 1200 20 L1200 95 L0 95Z" fill="#b38b45"/>
    <path d="M0 52 C250 82 520 100 760 92 C950 86 1100 56 1200 38 L1200 95 L0 95Z" fill="#fff"/>
    <path d="M0 32 C260 62 520 84 760 74 C950 66 1100 32 1200 12" fill="none" stroke="#fff" stroke-width="2" stroke-dasharray="5 4"/>
  </svg>
</section>

<h2 class="sec-title" style="top:770px">WE FOCUS ON THREE CUSTOMER SEGMENTS:</h2>
<div class="sec-rule" style="top:824px;background:#d8c29a"></div>

<div class="segment" style="left:100px"><div class="fill" role="img" aria-label="Embroidered towel sets in red and white with ribbons for couples" style="background:linear-gradient(120deg,#efe9e4 0%,#c9b7a8 40%,#a8262c 70%,#f2f0ee 100%)"></div></div>
<div class="segment" style="left:440px"><div class="fill" role="img" aria-label="Personalized towels wrapped as gifts for friends" style="background:linear-gradient(135deg,#8e6a2c,#9f7a38 50%,#7c5a22)"></div><a class="shop-now" href="#">SHOP NOW</a></div>
<div class="segment" style="left:777px"><div class="fill" role="img" aria-label="White cushion embroidered with a baby name and birth calendar" style="background:radial-gradient(ellipse 140px 95px at 50% 50%,#f3f1f3 0%,#d8d2d8 55%,#2c2c2f 100%)"></div></div>

<p class="segment-caption" style="left:100px">Lovers and marring couples</p>
<p class="segment-caption" style="left:440px">Close friends wishing to give<br>unique gifts</p>
<p class="segment-caption" style="left:777px">Moms with new born baby<br>personalized gifts</p>

<section class="products-band">
  <h2 class="sec-title" style="top:60px">LATEST PRODUCTS</h2>
  <div class="sec-rule" style="top:108px;background:#d8c29a"></div>
  <svg class="slider-arrow" style="left:96px;top:72px" width="16" height="30" viewBox="0 0 16 30"><path d="M14 2 L3 15 L14 28" fill="none" stroke="#333" stroke-width="2.5"/></svg>
  <svg class="slider-arrow" style="left:1084px;top:72px" width="16" height="30" viewBox="0 0 16 30"><path d="M2 2 L13 15 L2 28" fill="none" stroke="#333" stroke-width="2.5"/></svg>
</section>

<article class="product-card" style="left:100px">
  <div class="thumb" role="img" aria-label="Gray bathrobe and towels with light blue name embroidery" style="background:linear-gradient(135deg,#7d7d80,#5f6064 60%,#9fb4c2)"></div>
  <h3 class="product-name">Bathrobes And Towels</h3>
  <p class="product-desc">Proin nulla arcu nonummy luctuic tum ermentum lorem de.</p>
  <div class="product-foot"><span class="price gold">$35.90</span><a class="btn-cart gold" href="#">Add to Cart</a></div>
</article>
<article class="product-card" style="left:355px">
  <div class="thumb" role="img" aria-label="White towels with purple monogram embroidery and bows" style="background:linear-gradient(135deg,#b9a9bd,#efecef 55%,#6d4f74)"></div>
  <h3 class="product-name" style="color:#555">Personalized Embroidery</h3>
  <p class="product-desc">Proin nulla arcu nonummy luctuic tum ermentum lorem de.</p>
  <div class="product-foot"><span class="price">$20.90</span><a class="btn-cart" href="#">Add to Cart</a></div>
</article>
<article class="product-card" style="left:612px">
  <div class="thumb" role="img" aria-label="Navy and white towels with matching name embroidery" style="background:linear-gradient(135deg,#f1f1f3,#d9dbe3 45%,#1f2e5a 80%)"></div>
  <h3 class="product-name" style="color:#555">Pillows And Cushions</h3>
  <p class="product-desc">Proin nulla arcu nonummy luctuic tum ermentum lorem de.</p>
  <div class="product-foot"><span class="price">$20.90</span><a class="btn-cart" href="#">Add to Cart</a></div>
</article>
<article class="product-card" style="left:868px">
  <div class="thumb" role="img" aria-label="Cream cushion with embroidered birth date calendar" style="background:radial-gradient(ellipse 100px 80px at 50% 50%,#f6f1ea,#e4d8c8 70%,#a38e74)"></div>
  <h3 class="product-name" style="color:#555">Baby Gifts</h3>
  <p class="product-desc">Proin nulla arcu nonummy luctuic tum ermentum lorem de.</p>
  <div class="product-foot"><span class="price">$20.90</span><a class="btn-cart" href="#">Add to Cart</a></div>
</article>

<section class="gallery-band">
  <svg class="abs" style="left:0;top:6px" width="1200" height="4" aria-hidden="true"><line x1="0" y1="2" x2="1200" y2="2" stroke="#888" stroke-width="1.5" stroke-dasharray="5 4"/></svg>
  <h2 class="gallery-title">OUR GALLERY</h2>
  <div class="gallery-rule"></div>
  <div class="gallery-item" style="left:100px;top:167px;width:347px;height:349px;background:linear-gradient(160deg,#f4c3d6,#f3f0ec 45%,#d7c59a 70%,#b8465c)" role="img" aria-label="Baby gift basket with pink towel embroidered with a name"></div>
  <div class="gallery-item" style="left:474px;top:167px;width:300px;height:161px;background:linear-gradient(135deg,#8e1d2c,#a52739 60%,#7b1522)" role="img" aria-label="Burgundy towel with white script name embroidery"></div>
  <div class="gallery-item" style="left:798px;top:167px;width:302px;height:161px;background:linear-gradient(135deg,#6b6c78,#c2174f 60%,#e7e4ea)" role="img" aria-label="Stacked towels with pink and white name embroidery"></div>
  <div class="gallery-item" style="left:474px;top:355px;width:300px;height:161px;background:linear-gradient(135deg,#f6c9cf,#f3eeee 45%,#8fd9cf)" role="img" aria-label="Pink and mint towels with embroidered names"></div>
  <div class="gallery-item" style="left:798px;top:355px;width:302px;height:161px;background:linear-gradient(135deg,#f58f86,#f9b1a8 50%,#ece7e9)" role="img" aria-label="Coral towels with navy name embroidery and hearts"></div>
  <svg class="slider-arrow" style="left:38px;top:330px" width="20" height="36" viewBox="0 0 20 36"><path d="M17 2 L3 18 L17 34" fill="none" stroke="#fff" stroke-width="2.5"/></svg>
  <svg class="slider-arrow" style="left:1142px;top:330px" width="20" height="36" viewBox="0 0 20 36"><path d="M3 2 L17 18 L3 34" fill="none" stroke="#fff" stroke-width="2.5"/></svg>
</section>

<div class="feature" style="left:93px">
  <span class="feature-badge"><svg width="46" height="32" viewBox="0 0 46 32"><rect x="1" y="4" width="28" height="19" fill="#fff"/><path d="M29 10 L38 10 L44 17 L44 23 L29 23Z" fill="#fff"/><circle cx="10" cy="26" r="4.5" fill="#fff" stroke="#b38b45" stroke-width="2"/><circle cx="36" cy="26" r="4.5" fill="#fff" stroke="#b38b45" stroke-width="2"/></svg></span>
  <div><h3>FREE DELIVERY</h3><p>If you buy more then 100 USD<br>will be Free Delivery</p></div>
</div>
<div class="feature" style="left:425px">
  <span class="feature-badge" style="background:#6b6b6b;box-shadow:0 0 0 2px #6b6b6b;border-color:#ddd"><svg width="40" height="42" viewBox="0 0 40 42"><circle cx="20" cy="15" r="10" fill="#fff"/><path d="M8 15 C8 5 32 5 32 15" fill="none" stroke="#fff" stroke-width="3"/><path d="M4 42 C4 30 36 30 36 42Z" fill="#fff"/></svg></span>
  <div><h3>CUSTOMER CARE</h3><p>We Support You 24/7 You can<br>Email us in care@velvetloom.example</p></div>
</div>
<div class="feature" style="left:759px">
  <span class="feature-badge"><svg width="44" height="36" viewBox="0 0 44 36"><rect x="2" y="8" width="30" height="18" rx="2" fill="#fff"/><circle cx="17" cy="17" r="5" fill="#b38b45"/><circle cx="34" cy="26" r="9" fill="#fff" stroke="#b38b45" stroke-width="2"/><path d="M34 21 L34 31 M31 23 L37 23" stroke="#b38b45" stroke-width="2"/></svg></span>
  <div><h3>REFUND POLICY</h3><p>You Can Refund in 3 days After That You<br>Can Change It With in 14 Days Max</p></div>
</div>

<svg class="footer-wave" width="1200" height="130" viewBox="0 0 1200 130" aria-hidden="true">
  <path d="M0 70 C220 10 480 0 700 30 C900 56 1080 90 1200 110 L1200 130 L0 130Z" fill="#b38b45"/>
  <path d="M0 92 C220 32 480 22 700 52 C900 78 1080 110 1200 128 L1200 130 L0 130Z" fill="#343434"/>
  <path d="M0 104 C220 44 480 34 700 64 C900 90 1080 120 1200 136" fill="none" stroke="#aaa" stroke-width="1.5" stroke-dasharray="5 4"/>
</svg>

<footer class="site-footer">
  <div class="footer-brand"><span class="dot"></span>Velvet Loom</div>

  <h4 class="footer-head" style="left:372px">USEFULL LINKS</h4>
  <ul class="link-list">
    <li>&gt;&nbsp; Home</li><li>&gt;&nbsp; Embroidery</li><li>&gt;&nbsp; Products</li><li>&gt;&nbsp; Gallery</li><li>&gt;&nbsp; Shop</li><li>&gt;&nbsp; Contact Us</li>
  </ul>

  <h4 class="footer-head" style="left:548px">CONTACT US</h4>
  <div class="contact-row" style="top:125px">
    <span class="ring"><svg width="12" height="16" viewBox="0 0 12 16"><path d="M6 15 C2 10 1 8 1 6 A5 5 0 0 1 11 6 C11 8 10 10 6 15Z" fill="#fff"/><circle cx="6" cy="6" r="2" fill="#343434"/></svg></span>
    <div><strong>ADDRESS,</strong><span>58 Cedar Row, Al Nakheel,<br>SA</span></div>
  </div>
  <div class="contact-row" style="top:203px">
    <span class="ring"><svg width="10" height="16" viewBox="0 0 10 16"><rect x="1" y="1" width="8" height="14" rx="1.5" fill="none" stroke="#fff" stroke-width="1.6"/><circle cx="5" cy="12" r="1" fill="#fff"/></svg></span>
    <div><strong>PHONE NUMBER:</strong><span>+966 55 321 9076</span></div>
  </div>
  <div class="contact-row" style="top:273px">
    <span class="ring"><svg width="16" height="12" viewBox="0 0 16 12"><rect x="1" y="1" width="14" height="10" fill="#fff"/><path d="M1 1 L8 7 L15 1" fill="none" stroke="#343434" stroke-width="1.4"/></svg></span>
    <div><strong>EMAIL:</strong><span>Velvet.loom.atelier@stitchmail.example</span></div>
  </div>

  <h4 class="footer-head" style="left:834px;top:68px">PAYMENT OPTIONS</h4>
  <div class="pay-box" role="img" aria-label="Accepted payment methods: online wallet, cards and bank transfer">
    <span class="pay-chip" style="background:#1d3f8a"></span>
    <span class="pay-chip" style="background:#d9a531"></span>
    <span class="pay-chip" style="background:#cfd4da"></span>
  </div>

  <div class="footer-bar"></div>
  <p class="copyright">Copyrights © 2017 Velvet Loom. All Rights Reserved.</p>
  <div class="social" aria-label="Social links"><span></span><span></span><span></span><span></span><span></span></div>
</footer>

</body>
</html>
```